IT Professional business card with a hometown feel and a little edgy.

My business name is Tamble Website Solutions. But I have ended up doing much more. I live in a very small remote community, where everyone knows everyone. We like the one-on-one customer service in this community. I do computer tutoring, virus removal, networking, and software training. My clients are businesses and private individuals.

My website is tamblewebsitesolutions.example, when I first designed it I was going for a fresh, clean look, which I still like. But I am thinking about making the website a bit more edgy to match my new logo from ArtHively (logo attached). At this time my website does not display the new logo, but I plan on redesigning the website in the future to match the logo and business card.

My tag line is "put the web to work for you"

I'm thinking I would like to have the business card printed with a metallic finish.
Updates

Please do not use black backgrounds, or any solid dark colors. Prefer light or white backgrounds.

Target Market(s)

Small businesses. Individuals that need computer help at home.

Industry/Entity Type

It Company

Contact Information for Business Card

Nora Prandell
Tamble Website Solutions
PO Box 7153
Fernridge, WA 98412
Cell: 555-271-3096
nora@tamblewebsitesolutions.example
tamblewebsitesolutions.example

Font styles to use
Serif

Requirements
Must have
• Must have all the information listed in "Business Card Details"
• Must use the logo provided.
• Use the colors from the provided logo
Nice to have
• Would like to use my tagline "put the web to work for you" all lowercase

```html
<!DOCTYPE html>
<html lang="en">
<head>
<meta charset="utf-8">
<title>Tamble Website Solutions – Business Card</title>
<link rel="stylesheet" href="https://fonts.googleapis.com/css2?family=Nunito+Sans:wght@300;400&family=PT+Sans:ital@1&display=swap">
<style>
  :root {
    --page: #ffffff;
    --card: #ffffff;
    --green-light: #76c043;
    --green-dark: #2c6130;
    --green-text: #2f7a31;
    --ink: #4a4a4a;
    --ink-soft: #5a5a5a;
    --rule: #3a3a3a;
    --edge: #d8d8d8;
  }
  html, body {
    margin: 0;
    padding: 0;
    width: 998px;
    height: 1200px;
    overflow: hidden;
    background: var(--page);
  }
  .canvas {
    position: relative;
    width: 998px;
    height: 1200px;
  }
  .card {
    position: absolute;
    left: 94px;
    width: 818px;
    height: 471px;
    background: var(--card);
    box-sizing: border-box;
    box-shadow: 14px 16px 18px rgba(0, 0, 0, 0.35);
  }
  .card--front { top: 75px; }
  .card--back {
    top: 620px;
    height: 468px;
    border: 1px solid var(--edge);
    border-bottom: none;
  }
  .band {
    position: absolute;
    left: 0;
    right: 0;
  }
  .band--top { top: 0; height: 19px; background: var(--green-light); }
  .band--bottom { bottom: 0; height: 19px; background: var(--green-light); }
  .band--footer { bottom: 0; height: 16px; background: var(--green-dark); }

  .contact {
    position: absolute;
    top: 129px;
    left: 0;
    right: 0;
    text-align: center;
    font-family: "Nunito Sans", sans-serif;
    font-weight: 300;
    color: var(--ink);
  }
  .contact__name {
    margin: 0 0 14px;
    font-size: 31px;
    font-weight: 400;
    color: var(--green-text);
    line-height: 1.2;
  }
  .contact__lines {
    margin: 0;
    font-size: 21px;
    line-height: 32px;
  }
  .contact__lines + .contact__lines { margin-top: 17px; }

  .brand {
    position: absolute;
    top: 116px;
    left: 0;
    right: 0;
    height: 212px;
    display: flex;
    justify-content: center;
    align-items: center;
  }
  .brand__mark {
    width: 120px;
    height: 120px;
    background: var(--green-text);
    margin-right: 48px;
  }
  .brand__divider {
    width: 2px;
    height: 212px;
    background: var(--rule);
    margin-right: 26px;
  }
  .brand__name {
    margin: 0;
    font-family: "Nunito Sans", sans-serif;
    font-weight: 400;
    font-size: 33px;
    line-height: 37px;
    color: var(--ink-soft);
  }
  .tagline {
    position: absolute;
    top: 366px;
    left: 0;
    right: 0;
    margin: 0;
    text-align: center;
    font-family: "PT Sans", sans-serif;
    font-style: italic;
    font-size: 35px;
    color: var(--green-text);
  }
</style>
</head>
<body>
<main class="canvas">
  <section class="card card--front" aria-label="Card front">
    <div class="band band--top"></div>
    <div class="contact">
      <h1 class="contact__name">Nora Prandell</h1>
      <p class="contact__lines">
        Cell: 555-271-3096<br>
        nora@tamblewebsitesolutions.example<br>
        tamblewebsitesolutions.example
      </p>
      <p class="contact__lines">
        Tamble Website Solutions<br>
        PO Box 7153 Fernridge, WA 98412
      </p>
    </div>
    <div class="band band--bottom"></div>
  </section>

  <section class="card card--back" aria-label="Card back">
    <div class="brand">
      <div class="brand__mark" aria-hidden="true"></div>
      <div class="brand__divider" aria-hidden="true"></div>
      <p class="brand__name">Tamble<br>Website<br>Solutions</p>
    </div>
    <p class="tagline">put the web to work for you</p>
    <div class="band band--footer"></div>
  </section>
</main>
</body>
</html>
```